Cork Lantern website design elements

Company: Cork Lantern
Business: Wine website (selling wine online)
www.corklantern-demo.com.au
Please note that this is an initial project, ongoing design work will be required after this project.
Design requirement
Note: Full website design not required, only specific elements to enhance current design.
- Must work with existing logo and wood background (do not change site background)
- Must work with a orange (please improve current orange colour) and blue colour (blue colour in attachments)
- Pictures of wine bottles or wine glasses are not to be used in design elements.
I currently have an existing design which I would like certain elements designed for. Design elements must work with responsive functionality.
I am trying to achieve a modern retro feel of the website, please refer to the below websites as examples that I am trying to look like.
- https://au.brisktrimhouse-demo.com/
- http://www.kestrelmarlow-demo.com/italian/australia/home
- http://www.tangerinefizz-demo.co.uk/
- http://www.codeharbour-demo.org.nz/13/
As mentioned the site is already built and I need certain elements to work with what is already there. All elements must work with current logo and wood panel background.
I require the following elements
• Menu bar (must be the orange)
• Home page promo slider (Text, this weeks special etc)
• 2x homepage promo tabs buttons (Join the lantern club, what's in the box deal)
• 4x Homepage navigation tabs (Red wine, White wine, Sparkling, Pre mixed cases)
• Add to cart button
• Product image backdrop (can be wider than current examples)
o I would like the backdrops to be a different colour scheme to each other e.g red wine will habe red colour, white will have a cream colour, etc)
o I would prefer a close up of the product, does not need to be full view
Please refer to attachments for elements that I like and would like to mimic.
Colour scheme
- Use existing orange (please suggest if you think of a better tone)
- Secondary colour light baby blue (suggest best options)
- Please advise of other colours needed
Design elements to be provided in jog and raw design format.
This project will require ongoing work.
I will provide access details to site upon request.
Please contact me if you have any questions.
Tobias
Cork Lantern

```html
<!DOCTYPE html>
<html lang="en">
<head>
<meta charset="utf-8">
<title>Cork Lantern — Home</title>
<link rel="stylesheet" href="https://fonts.googleapis.com/css2?family=Alfa+Slab+One&family=Amatic+SC:wght@700&family=Bebas+Neue&family=Big+Shoulders+Display:wght@500&family=Josefin+Sans:wght@600&family=Open+Sans:wght@400&display=swap">
<style>
  :root {
    --orange: #f26a1b;
    --teal: #5e9ea3;
    --teal-light: #86bfc1;
    --teal-dark: #4a8a90;
    --wood-a: #8a5a36;
    --wood-b: #6e4326;
    --wood-c: #a06b43;
    --ink: #1f1f1f;
    --cream: #fbf6ea;
    --red: #b3262b;
    --maroon: #6f2a2f;
    --slate: #4c585c;
    --charcoal: #232323;
    --green: #2f6b45;
    --olive: #7d7c3f;
    --plum: #4e2540;
    --white: #ffffff;
  }
  * { box-sizing: border-box; margin: 0; padding: 0; }
  html, body { width: 1200px; height: 746px; overflow: hidden; background: var(--white); }
  .page { position: relative; width: 1200px; height: 746px; }

  .wood {
    position: absolute; left: 0; top: 0; width: 1200px; height: 605px;
    background:
      repeating-linear-gradient(90deg, rgba(0,0,0,0.12) 0 2px, transparent 2px 150px),
      linear-gradient(90deg, var(--wood-b), var(--wood-c) 25%, var(--wood-a) 50%, var(--wood-c) 75%, var(--wood-b));
    border-top: 5px solid var(--orange);
  }

  .brand {
    position: absolute; left: 122px; top: 38px;
    display: flex; align-items: center; gap: 10px;
    font-family: "Josefin Sans", sans-serif; font-weight: 600;
    font-size: 26px; color: var(--white); letter-spacing: 1px; white-space: nowrap;
  }
  .brand-dot { width: 16px; height: 16px; border-radius: 50%; background: var(--orange); }

  .search {
    position: absolute; left: 455px; top: 50px; width: 292px; height: 30px;
    background: var(--white); border: 1px solid #ccc;
    font-family: "Open Sans", sans-serif; font-size: 11px; color: #999;
    padding: 8px 10px; white-space: nowrap;
  }
  .search svg { position: absolute; right: 10px; top: 8px; }

  .cart {
    position: absolute; left: 994px; top: 58px;
    font-family: "Open Sans", sans-serif; font-size: 11px; color: var(--white);
    display: flex; align-items: center; gap: 6px; white-space: nowrap;
  }

  .panel {
    position: absolute; left: 99px; top: 115px; width: 1004px; height: 478px;
    background: var(--teal);
  }

  .menu {
    position: absolute; left: 12px; top: 12px; width: 980px; height: 60px;
    background: var(--teal-light);
    border-top: 7px solid var(--white); border-bottom: 7px solid var(--white);
    display: flex; align-items: center; padding-left: 39px;
    font-family: "Josefin Sans", sans-serif; font-weight: 600; font-size: 21px; letter-spacing: 1.5px;
    color: var(--ink); white-space: nowrap;
  }
  .menu-item { position: relative; padding-top: 4px; }
  .menu-item.is-active { color: var(--orange); }
  .menu-item.is-active::after {
    content: ""; position: absolute; left: -39px; right: -50px; bottom: -16px;
    height: 8px; background: var(--orange);
  }
  .menu-sep { margin: 0 30px; padding-top: 4px; }

  .hero {
    position: absolute; left: 11px; top: 90px; width: 660px; height: 242px;
    background: var(--teal-light);
    border: 2px solid var(--teal-dark);
    overflow: hidden;
  }
  .hero-price {
    position: absolute; left: 34px; top: 8px;
    font-family: "Big Shoulders Display", sans-serif; font-weight: 500;
    font-size: 210px; line-height: 1; color: var(--red); letter-spacing: -4px; white-space: nowrap;
  }
  .hero-mixed {
    position: absolute; left: 318px; top: 6px; width: 300px; text-align: center;
    font-family: "Alfa Slab One", serif; font-size: 54px; line-height: 1.35; color: var(--cream);
    border-bottom: 2px solid var(--red); padding-bottom: 2px; white-space: nowrap;
  }
  .hero-count {
    position: absolute; left: 440px; top: 96px; width: 56px; height: 56px; border-radius: 50%;
    background: #a96a4a; color: var(--teal-light);
    font-family: "Alfa Slab One", serif; font-size: 36px; text-align: center; line-height: 56px;
  }
  .hero-cases {
    position: absolute; left: 318px; top: 162px; width: 300px; text-align: center;
    font-family: "Bebas Neue", sans-serif; font-size: 62px; line-height: 1; color: var(--ink);
    white-space: nowrap;
  }

  .promo { position: absolute; }
  .promo-club { left: 689px; top: 95px; width: 300px; height: 105px; }
  .promo-box { left: 689px; top: 215px; width: 300px; height: 117px; }
  .promo svg { position: absolute; left: 0; top: 0; }
  .club-text {
    position: absolute; left: 88px; top: 14px;
    font-family: "Amatic SC", sans-serif; font-weight: 700; font-size: 38px; line-height: 0.95;
    color: var(--cream); letter-spacing: 1px; white-space: nowrap;
  }
  .club-icon {
    position: absolute; left: 22px; top: 30px; width: 50px; height: 44px;
    border-radius: 22px; background: #c9c6a0;
  }
  .box-text {
    position: absolute; left: 0; top: 64px; width: 300px; text-align: center;
    font-family: "Bebas Neue", sans-serif; font-size: 36px; color: var(--red); letter-spacing: 1px;
    white-space: nowrap;
  }
  .box-text span { color: var(--orange); }

  .tab { position: absolute; top: 358px; width: 230px; height: 110px; }
  .tab svg { position: absolute; left: 0; top: 0; }
  .tab-label {
    position: absolute; left: 0; top: 0; width: 190px; height: 110px;
    display: flex; align-items: center; justify-content: center; text-align: center;
    font-family: "Bebas Neue", sans-serif; font-size: 42px; line-height: 0.9; color: var(--cream);
    white-space: nowrap;
  }
  .tab-red { left: 11px; } .tab-white { left: 261px; }
  .tab-sparkling { left: 518px; } .tab-cases { left: 761px; }
  .tab-cases .tab-label { font-size: 34px; }
  .tab-cases .tab-label b { font-family: "Alfa Slab One", serif; font-weight: 400; font-size: 34px; display: block; }
</style>
</head>
<body>
<div class="page">
  <div class="wood">
    <div class="brand"><span class="brand-dot"></span>Cork Lantern</div>

    <div class="search">Search entire store here...
      <svg width="12" height="12" viewBox="0 0 12 12"><circle cx="5" cy="5" r="3.8" fill="none" stroke="#999" stroke-width="1.4"/><line x1="8" y1="8" x2="11" y2="11" stroke="#999" stroke-width="1.4"/></svg>
    </div>

    <div class="cart">
      <svg width="10" height="12" viewBox="0 0 10 12"><rect x="0" y="3" width="10" height="9" fill="#fff"/><path d="M3 4V2a2 2 0 0 1 4 0v2" fill="none" stroke="#fff" stroke-width="1.2"/></svg>
      Cart AU$0.00
    </div>

    <div class="panel">
      <nav class="menu">
        <span class="menu-item is-active">HOME</span><span class="menu-sep">/</span>
        <span class="menu-item">RED WINE</span><span class="menu-sep">/</span>
        <span class="menu-item">WHITE WINE</span><span class="menu-sep">/</span>
        <span class="menu-item">SPARKLING</span><span class="menu-sep">/</span>
        <span class="menu-item">MIXED CASES</span>
      </nav>

      <section class="hero">
        <div class="hero-price">$149</div>
        <div class="hero-mixed">mixed</div>
        <div class="hero-count">6</div>
        <div class="hero-cases">BOTTLE CASES</div>
      </section>

      <a class="promo promo-club">
        <svg width="300" height="105" viewBox="0 0 300 105">
          <polygon points="0,0 300,0 262,52 300,105 0,105" fill="var(--teal-dark)"/>
          <polygon points="0,0 278,0 245,52 278,105 0,105" fill="var(--olive)"/>
        </svg>
        <div class="club-icon" role="img" aria-label="Club members illustration"></div>
        <div class="club-text">JOIN THE<br>LANTERN CLUB</div>
      </a>

      <a class="promo promo-box">
        <svg width="300" height="117" viewBox="0 0 300 117">
          <polygon points="0,45 150,0 300,45 300,117 0,117" fill="var(--plum)"/>
          <polygon points="12,52 150,12 288,52 288,106 12,106" fill="none" stroke="var(--teal-light)" stroke-width="3"/>
          <rect x="12" y="62" width="276" height="44" fill="var(--teal-light)"/>
        </svg>
        <div class="box-text">MISTERY <span>BOX DEAL</span></div>
      </a>

      <a class="tab tab-red">
        <svg width="230" height="110" viewBox="0 0 230 110"><polygon points="0,0 230,0 200,55 230,110 0,110" fill="var(--teal-dark)"/><polygon points="0,0 210,0 182,55 210,110 0,110" fill="var(--maroon)"/></svg>
        <div class="tab-label">RED WINE</div>
      </a>
      <a class="tab tab-white">
        <svg width="230" height="110" viewBox="0 0 230 110"><polygon points="0,0 230,0 200,55 230,110 0,110" fill="var(--teal-dark)"/><polygon points="0,0 210,0 182,55 210,110 0,110" fill="var(--slate)"/></svg>
        <div class="tab-label">WHITE WINE</div>
      </a>
      <a class="tab tab-sparkling">
        <svg width="230" height="110" viewBox="0 0 230 110"><polygon points="0,0 230,0 200,55 230,110 0,110" fill="var(--teal-dark)"/><polygon points="0,0 210,0 182,55 210,110 0,110" fill="var(--charcoal)"/></svg>
        <div class="tab-label">SPARKLING</div>
      </a>
      <a class="tab tab-cases">
        <svg width="230" height="110" viewBox="0 0 230 110"><polygon points="0,0 230,0 200,55 230,110 0,110" fill="var(--teal-dark)"/><polygon points="0,0 210,0 182,55 210,110 0,110" fill="var(--green)"/></svg>
        <div class="tab-label"><span><b>PRE</b>MIXED CASES</span></div>
      </a>
    </div>
  </div>
</div>
</body>
</html>
```